Bramble Artisan Wood Fired Pizza business card design

I have a logo and need an eye catching design that will get me noticed.
My business is wood fired pizza. I want a bold design that will make our customers remember us and the food that we serve. Work with the colors of our logo and texts. Maybe add designs that lend to what or how pizza is made using our wood fired oven?

Target Market(s)

Foodies!

Contact Information for Business Card

Bramble Artisan Wood Fired Pizza
Our slogan is Fast. Fresh. Handcrafted
Catering for all events

Requirements
Must have
• Noel Pruett
Telephone 570 555 0187
website www.trybramble.com
Facebook @trybramblepizza maybe use the facebook logo next to it
Instagram trybramblepizza maybe use the instagram logo next to it
Catering for all events
Nice to have
• Maybe pizza peels, pizza cutters? Wood? Fired wood? Using our flame in the background?
Please work with different colored text so each sentence stands out? A themed color for facebook?
Maybe work with the colors within our logo?
Please try to use the our bramble font, but not a must have.

```html
<!DOCTYPE html>
<html lang="en">
<head>
<meta charset="utf-8">
<title>Bramble Artisan Wood Fired Pizza – Business Cards</title>
<link href="https://fonts.googleapis.com/css2?family=Almendra&family=Oswald:wght@700&family=Roboto+Condensed:wght@400;700&family=Open+Sans:wght@400&display=swap" rel="stylesheet">
<style>
  :root{
    --page:#eceeed;
    --gold-deep:#ffb000;
    --gold-light:#ffe57a;
    --maroon:#722e2e;
    --orange:#f0921a;
    --red:#d7262b;
    --ink:#1d1b18;
    --silver-light:#fafafa;
    --silver-deep:#cfcfcf;
    --text-dark:#2a2a2a;
    --white:#ffffff;
  }
  *{margin:0;padding:0;box-sizing:border-box}
  html,body{width:1200px;height:837px;overflow:hidden;background:var(--page)}
  .sheet{position:relative;width:1200px;height:837px}
  .card{position:absolute;width:430px;height:248px;border-radius:12px;overflow:hidden;
        box-shadow:0 4px 10px rgba(0,0,0,.18)}
  .card svg.card-bg{position:absolute;inset:0;width:100%;height:100%}
  .col-left{left:122px}.col-right{left:648px}
  .row-top{top:150px}.row-bottom{top:428px}

  .gold{background:linear-gradient(160deg,var(--gold-deep) 0%,var(--gold-light) 45%,var(--gold-deep) 100%)}
  .silver{background:linear-gradient(160deg,var(--silver-deep) 0%,var(--silver-light) 45%,var(--silver-deep) 100%)}

  .holder-name{position:absolute;top:12px;left:0;right:0;text-align:center;
    font-family:"Almendra",serif;font-size:29px;color:var(--red);letter-spacing:.5px}
  .brand{position:absolute;left:0;right:0;display:flex;flex-direction:column;align-items:center}
  .brand-mark{width:34px;height:34px;border-radius:50%;background:var(--red)}
  .brand-name{font-family:"Oswald",sans-serif;font-weight:700;color:var(--red);
    font-size:26px;letter-spacing:3px;line-height:1;margin-top:6px}
  .front .brand{top:58px}

  .slogan{position:absolute;left:0;right:0;text-align:center;top:180px;
    font-family:"Roboto Condensed",sans-serif;font-weight:700;font-size:21px;line-height:1}
  .gold-front .slogan{color:var(--orange)}
  .silver-front .slogan{color:var(--white)}
  .slogan .dot{color:var(--red);margin:0 4px}
  .catering{position:absolute;left:0;right:0;text-align:center;top:206px;
    font-family:"Roboto Condensed",sans-serif;font-size:21px;color:var(--white);line-height:1}

  .back .brand{left:20px;right:auto;width:180px;top:78px}
  .back .brand-mark{width:44px;height:44px}
  .divider{position:absolute;left:187px;top:78px;width:2px;height:92px;background:var(--orange)}
  .contacts{position:absolute;left:214px;top:76px;list-style:none;
    font-family:"Open Sans",sans-serif;font-size:14.5px;color:var(--text-dark)}
  .contacts li{display:flex;align-items:center;height:24px}
  .contacts svg{width:12px;height:12px;margin-right:6px;flex:none}
</style>
</head>
<body>
<main class="sheet">

  <section class="card front gold gold-front col-left row-top">
    <svg class="card-bg" viewBox="0 0 430 248" preserveAspectRatio="none" aria-hidden="true">
      <path d="M0,50 C100,50 130,100 150,135 C165,160 185,165 215,165 C245,165 265,160 280,135 C310,85 370,20 430,10 L430,248 L0,248 Z" fill="var(--maroon)"/>
      <path d="M0,50 C100,50 130,100 150,135 C165,160 185,165 215,165 C245,165 265,160 280,135 C310,85 370,20 430,10" fill="none" stroke="var(--orange)" stroke-width="6"/>
    </svg>
    <h2 class="holder-name">NOEL PRUETT</h2>
    <div class="brand"><span class="brand-mark"></span><span class="brand-name">BRAMBLE</span></div>
    <p class="slogan">Fast<span class="dot">·</span>Fresh<span class="dot">·</span>Handcrafted</p>
    <p class="catering">Catering for all events</p>
  </section>

  <section class="card front silver silver-front col-right row-top">
    <svg class="card-bg" viewBox="0 0 430 248" preserveAspectRatio="none" aria-hidden="true">
      <path d="M0,15 C90,35 125,95 150,135 C165,160 185,165 215,165 C245,165 265,160 280,135 C320,95 375,72 430,68 L430,248 L0,248 Z" fill="var(--ink)"/>
      <path d="M0,15 C90,35 125,95 150,135 C165,160 185,165 215,165 C245,165 265,160 280,135 C320,95 375,72 430,68" fill="none" stroke="var(--red)" stroke-width="6"/>
    </svg>
    <h2 class="holder-name">NOEL PRUETT</h2>
    <div class="brand"><span class="brand-mark"></span><span class="brand-name">BRAMBLE</span></div>
    <p class="slogan">Fast<span class="dot">·</span>Fresh<span class="dot">·</span>Handcrafted</p>
    <p class="catering">Catering for all events</p>
  </section>

  <section class="card back gold col-left row-bottom">
    <div class="brand"><span class="brand-mark"></span><span class="brand-name">BRAMBLE</span></div>
    <span class="divider"></span>
    <ul class="contacts">
      <li><svg viewBox="0 0 12 12"><path d="M2.5 1l2 2.2-1 1.3c.6 1.5 1.7 2.6 3.1 3.2l1.3-1 2.1 2-1 1.8C5 10.3 1.7 7 1 2z" fill="var(--red)"/></svg>570 555 0187</li>
      <li><svg viewBox="0 0 12 12"><circle cx="6" cy="6" r="5" fill="none" stroke="var(--red)" stroke-width="1.2"/><path d="M1 6h10M6 1c-2.5 3-2.5 7 0 10M6 1c2.5 3 2.5 7 0 10" fill="none" stroke="var(--red)" stroke-width="1"/></svg>www.trybramble.com</li>
      <li><svg viewBox="0 0 12 12"><circle cx="6" cy="6" r="5.5" fill="var(--red)"/></svg>@trybramblepizza</li>
      <li><svg viewBox="0 0 12 12"><circle cx="6" cy="6" r="5.5" fill="var(--red)"/></svg>trybramblepizza</li>
    </ul>
  </section>

  <section class="card back silver col-right row-bottom">
    <div class="brand"><span class="brand-mark"></span><span class="brand-name">BRAMBLE</span></div>
    <span class="divider"></span>
    <ul class="contacts">
      <li><svg viewBox="0 0 12 12"><path d="M2.5 1l2 2.2-1 1.3c.6 1.5 1.7 2.6 3.1 3.2l1.3-1 2.1 2-1 1.8C5 10.3 1.7 7 1 2z" fill="var(--red)"/></svg>570 555 0187</li>
      <li><svg viewBox="0 0 12 12"><circle cx="6" cy="6" r="5" fill="none" stroke="var(--red)" stroke-width="1.2"/><path d="M1 6h10M6 1c-2.5 3-2.5 7 0 10M6 1c2.5 3 2.5 7 0 10" fill="none" stroke="var(--red)" stroke-width="1"/></svg>www.trybramble.com</li>
      <li><svg viewBox="0 0 12 12"><circle cx="6" cy="6" r="5.5" fill="var(--red)"/></svg>@trybramblepizza</li>
      <li><svg viewBox="0 0 12 12"><circle cx="6" cy="6" r="5.5" fill="var(--red)"/></svg>trybramblepizza</li>
    </ul>
  </section>

</main>
</body>
</html>
```